Customs House descriptive business cards

We require a two-sided business card that has a simple yet elegant design. We want to be able to promote our services as a customs house. This card should include our logo, contact info and services offered with the logo being on one side and the contact info and services on the flip side

Target Market(s)

Importers / exporters to and from the Bahamas

Industry/Entity Type

Logistics

Contact Information for Business Card

The front side of the card could have the logo and the flip side should have the other relevant info

Font styles to use
Serif

Colors

Designer to choose colors to be used in the design.

Requirements
Must have
• (Harbourline Agents Ltd) Logo, address and contact info also services:
• import customs clearance, Delivery & HAndling services,Florida pickups, Export packing & Crating Services, export customs clearance, Consulting

```html
<!DOCTYPE html>
<html lang="en">
<head>
<meta charset="utf-8">
<title>Harbourline Agents Ltd – Business Card</title>
<link rel="stylesheet" href="https://fonts.googleapis.com/css2?family=Crimson+Text:wght@400;600&display=swap">
<style>
  :root {
    --page-bg: #e4e8ee;
    --card-light: #f3f5f8;
    --blue-deep: #1c4a9e;
    --blue-mid: #2556ad;
    --band-blue: #2f6db6;
    --band-text: #0f1d36;
    --name-grey: #b9bec6;
    --soft-grey: #aab6cc;
    --white: #ffffff;
    --bullet: #b8c2d2;
    --mark-tint: #dfe5ee;
  }
  * { box-sizing: border-box; margin: 0; padding: 0; }
  html, body {
    width: 1200px; height: 782px; overflow: hidden;
    background: var(--page-bg);
    font-family: "Crimson Text", Georgia, serif;
  }
  .card {
    position: absolute; left: 80px; top: 94px;
    width: 1040px; height: 594px;
    background: var(--card-light);
    overflow: hidden;
    box-shadow: 0 10px 30px rgba(20, 40, 80, 0.18);
  }
  .card__field { position: absolute; inset: 0; width: 100%; height: 100%; }
  .card__mark-spot {
    position: absolute; left: 60px; top: 180px;
    width: 220px; height: 220px; border-radius: 50%;
    background: var(--mark-tint);
  }
  .holder {
    position: absolute; right: 36px; top: 28px; text-align: right;
  }
  .holder__name {
    font-size: 41px; letter-spacing: 2px; color: var(--name-grey);
    font-weight: 400; line-height: 1.1;
  }
  .holder__role { font-size: 21px; color: var(--white); letter-spacing: 0.5px; }
  .company {
    position: absolute; right: 36px; top: 158px; text-align: right;
    color: var(--white); font-weight: 400;
  }
  .company__main { font-size: 62px; line-height: 1; letter-spacing: 1px; }
  .company__rule { height: 1px; background: rgba(255,255,255,0.6); margin: 6px 0 4px; }
  .company__sub { font-size: 25px; letter-spacing: 6px; }
  .contact {
    position: absolute; right: 36px; top: 304px; text-align: right;
    color: var(--soft-grey); font-size: 22px; line-height: 31px;
  }
  .contact__address { margin-bottom: 8px; }
  .contact__row { display: flex; justify-content: flex-end; align-items: center; gap: 12px; }
  .contact__icon { width: 16px; height: 16px; flex: none; }
  .services {
    position: absolute; left: 0; right: 0; bottom: 0; height: 99px;
    background: var(--band-blue);
    border-top: 2px solid rgba(255,255,255,0.25);
    padding: 14px 36px 0 44px;
    color: var(--band-text); font-size: 21px; line-height: 32px;
  }
  .services__row { display: flex; justify-content: space-between; list-style: none; }
  .services__item { display: flex; align-items: center; gap: 12px; }
  .services__item::before {
    content: ""; width: 7px; height: 7px; border-radius: 50%; background: var(--bullet);
  }
</style>
</head>
<body>
  <article class="card">
    <svg class="card__field" viewBox="0 0 1040 594" preserveAspectRatio="none" aria-hidden="true">
      <defs>
        <linearGradient id="panelBlue" x1="0" y1="0" x2="1" y2="1">
          <stop offset="0" stop-color="var(--blue-mid)"/>
          <stop offset="1" stop-color="var(--blue-deep)"/>
        </linearGradient>
      </defs>
      <polygon points="239,0 1040,0 1040,594 391,594" fill="url(#panelBlue)"/>
    </svg>

    <div class="card__mark-spot" aria-hidden="true"></div>

    <header class="holder">
      <h1 class="holder__name">MARCUS ELLERY</h1>
      <p class="holder__role">Founder &amp; CEO</p>
    </header>

    <div class="company">
      <div class="company__main">HARBOURLINE</div>
      <div class="company__rule"></div>
      <div class="company__sub">AGENTS LTD</div>
    </div>

    <address class="contact" style="font-style:normal">
      <div class="contact__address">48 Quayside Row, Suite# B<br>Nassau, NP 2041B7</div>
      <div class="contact__row">555 014 2290
        <svg class="contact__icon" viewBox="0 0 16 16"><path d="M4 1.5 6 4.5 4.8 6a8 8 0 0 0 5.2 5.2L11.5 10l3 2-1 2.5C7.5 14.5 1.5 8.5 1.5 2.5Z" fill="none" stroke="currentColor" stroke-width="1.4"/></svg>
      </div>
      <div class="contact__row">info@harbourline.com
        <svg class="contact__icon" viewBox="0 0 16 16"><rect x="1.5" y="3.5" width="13" height="9" fill="currentColor"/><path d="M1.5 3.5 8 9l6.5-5.5" fill="none" stroke="var(--blue-deep)" stroke-width="1.2"/></svg>
      </div>
      <div class="contact__row">www.harbourline.com
        <svg class="contact__icon" viewBox="0 0 16 16" fill="none" stroke="currentColor" stroke-width="1.3"><circle cx="8" cy="8" r="6.5"/><ellipse cx="8" cy="8" rx="2.8" ry="6.5"/><path d="M1.5 8h13"/></svg>
      </div>
    </address>

    <section class="services" aria-label="Services">
      <ul class="services__row">
        <li class="services__item">Import customs clearance</li>
        <li class="services__item">Delivery &amp; Handling services</li>
        <li class="services__item">Florida pickups</li>
      </ul>
      <ul class="services__row">
        <li class="services__item">Export Packing &amp; Crating Services</li>
        <li class="services__item">Export customs clearance</li>
        <li class="services__item">Consulting</li>
      </ul>
    </section>
  </article>
</body>
</html>
```